Weather card for guests at Marlow’s Shore Cottage

I am looking to have a card designed for my guests who stay over. The card should show the weather for the next day (emoji's), quote of the day, Activities of the day. It's for a beach house so it should be coastal/Beachy themed. The weather should have a high and a low. (I will fill in each card). It should be front and back. It should be a fun project. Think modern farmhouse. The top of each card should say something like Another great Day at 7 Harbor
Updates

If you google "turn down Service letter" or "hotel weather card". It will provide examples

Target Market(s)

Our guests who visit our beach house

Font styles to use
Sans Serif

Colors
0054AA
0677BA
7BADD7
CADEEF
E8F1F8

Requirements
Must have
• weather options, quote of the day, activity for the day
Nice to have
• Sand, seashells, seagulls
Should not have
• Should not be too busy and not childish

```html
<!DOCTYPE html>
<html lang="en">
<head>
<meta charset="utf-8">
<title>Marlow’s Shore Cottage – Guest Weather Card</title>
<link rel="stylesheet" href="https://fonts.googleapis.com/css2?family=Quicksand:wght@400;500;700&display=swap">
<style>
  :root {
    --navy: #0054AA;
    --ocean: #0677BA;
    --sky: #7BADD7;
    --mist: #CADEEF;
    --foam: #E8F1F8;
    --white: #ffffff;
    --sand: #ddd3cd;
    --backdrop: #ececec;
  }
  * { box-sizing: border-box; margin: 0; padding: 0; }
  html, body { width: 1200px; height: 993px; overflow: hidden; }
  body {
    background: var(--backdrop);
    position: relative;
    font-family: "Quicksand", sans-serif;
  }
  .card {
    position: absolute;
    width: 518px;
    height: 828px;
    overflow: hidden;
  }
  .card--front { left: 51px; top: 62px; }
  .card--back { left: 631px; top: 103px; }

  .card__scene {
    position: absolute; inset: 0;
    background: linear-gradient(to bottom,
      #1c63bd 0%,
      #3f86d2 22%,
      #6fa6dc 34%,
      #3f88cf 39.4%,
      #0c4f95 39.6%,
      #1591cc 44%,
      #22b3d6 52%,
      #74cfdc 60%,
      #eef4f5 65%,
      #f4f2ef 68%,
      #e3dad3 71%,
      #ddd3cd 85%,
      #d9cfc9 100%);
  }

  .headline {
    position: absolute;
    left: 0; right: 0; top: 78px;
    text-align: center;
    color: var(--white);
  }
  .headline__lead {
    display: block;
    font-weight: 700;
    font-size: 36px;
    letter-spacing: 0.3px;
    line-height: 1;
  }
  .headline__place {
    display: block;
    font-weight: 500;
    font-size: 108px;
    line-height: 1;
    margin-top: 4px;
    letter-spacing: -1px;
  }

  .section-title {
    position: absolute;
    left: 0; right: 0;
    text-align: center;
    color: var(--navy);
    font-weight: 700;
    font-size: 20px;
    line-height: 1;
  }
  .section-title--forecast { top: 561px; }
  .section-title--temps { top: 702px; }

  .forecast {
    position: absolute;
    left: 28px; top: 595px;
    display: flex; gap: 19px;
  }
  .forecast__option {
    position: relative;
    width: 77px; height: 77px;
    border: 1.5px solid var(--ocean);
    border-radius: 7px;
  }
  .forecast__check {
    position: absolute;
    right: 3px; top: 3px;
    width: 15px; height: 15px;
    border: 1.5px solid var(--ocean);
    border-radius: 50%;
    background: rgba(255,255,255,0.3);
  }
  .forecast__option svg { width: 77px; height: 77px; display: block; }
  .forecast__option svg * {
    fill: none; stroke: var(--ocean); stroke-width: 2; stroke-linecap: round; stroke-linejoin: round;
  }

  .temp {
    position: absolute;
    top: 731px;
    width: 220px; height: 37px;
    border: 1.5px solid var(--ocean);
    border-radius: 8px;
    padding: 9px 8px;
    color: var(--ocean);
    font-weight: 700;
    font-size: 14px;
    line-height: 1;
  }
  .temp--high { left: 28px; }
  .temp--low { left: 268px; }

  .note-box {
    position: absolute;
    left: 30px; width: 457px; height: 204px;
    border: 2px solid var(--sky);
    border-radius: 8px;
    background: linear-gradient(to bottom, rgba(232,241,248,0.78), rgba(255,255,255,0.55));
    text-align: center;
    padding-top: 10px;
  }
  .note-box--quote { top: 372px; }
  .note-box--activities { top: 592px; background: rgba(248,246,245,0.8); }
  .note-box__title {
    color: var(--navy);
    font-weight: 700;
    font-size: 20px;
    line-height: 1;
  }
</style>
</head>
<body>

<section class="card card--front">
  <div class="card__scene" role="img" aria-label="Photo of a tropical beach: blue sky with white clouds, turquoise sea, white surf and pale sand"></div>
  <h1 class="headline">
    <span class="headline__lead">Another great day at</span>
    <span class="headline__place">7 Harbor</span>
  </h1>

  <h2 class="section-title section-title--forecast">Weather Forecast</h2>
  <div class="forecast">
    <div class="forecast__option" aria-label="Sunny">
      <svg viewBox="0 0 77 77">
        <circle cx="38" cy="42" r="12"/>
        <path d="M38 23v-6M38 61v6M19 42h-6M57 42h6M24.5 28.5l-4-4M51.5 55.5l4 4M51.5 28.5l4-4M24.5 55.5l-4 4"/>
      </svg>
      <span class="forecast__check"></span>
    </div>
    <div class="forecast__option" aria-label="Partly cloudy">
      <svg viewBox="0 0 77 77">
        <path d="M22 40a8 8 0 1 1 11-9"/>
        <path d="M24 23v-3M13 34h-3M16 26l-2-2M31 26l2-2M16 42l-2 2"/>
        <path d="M24 57h38a7 7 0 0 0 0-14 10 10 0 0 0-19-4 8 8 0 0 0-13 5 7 7 0 0 0-6 13z"/>
      </svg>
      <span class="forecast__check"></span>
    </div>
    <div class="forecast__option" aria-label="Cloudy">
      <svg viewBox="0 0 77 77">
        <path d="M21 54h36a8 8 0 0 0 0-16 12 12 0 0 0-23-4 9 9 0 0 0-7 7 6.5 6.5 0 0 0-6 13z"/>
      </svg>
      <span class="forecast__check"></span>
    </div>
    <div class="forecast__option" aria-label="Rain">
      <svg viewBox="0 0 77 77">
        <path d="M21 46h36a8 8 0 0 0 0-16 12 12 0 0 0-23-4 9 9 0 0 0-7 7 6.5 6.5 0 0 0-6 13z"/>
        <path d="M23 54l-2.5 4a2.5 2.5 0 1 0 5 0zM38 54l-2.5 4a2.5 2.5 0 1 0 5 0zM53 54l-2.5 4a2.5 2.5 0 1 0 5 0z"/>
      </svg>
      <span class="forecast__check"></span>
    </div>
    <div class="forecast__option" aria-label="Snow">
      <svg viewBox="0 0 77 77">
        <path d="M38 18v48M17 30l42 24M17 54l42-24"/>
        <path d="M33 21l5 5 5-5M33 63l5-5 5 5M17 36l6-1-2-6M59 48l-6 1 2 6M21 55l2-6-6-1M55 29l-2 6 6 1"/>
      </svg>
      <span class="forecast__check"></span>
    </div>
  </div>

  <h2 class="section-title section-title--temps">Temperatures</h2>
  <div class="temp temp--high">High</div>
  <div class="temp temp--low">Low</div>
</section>

<section class="card card--back">
  <div class="card__scene" role="img" aria-label="Photo of a tropical beach: blue sky with white clouds, turquoise sea, white surf and pale sand"></div>
  <h1 class="headline">
    <span class="headline__lead">Another great day at</span>
    <span class="headline__place">7 Harbor</span>
  </h1>

  <div class="note-box note-box--quote">
    <h2 class="note-box__title">Quote of the day</h2>
  </div>
  <div class="note-box note-box--activities">
    <h2 class="note-box__title">Activities for the day</h2>
  </div>
</section>

</body>
</html>
```